Social Media Graphics - ALL TEXT RK

We are looking for a series of social media graphics for Instagram (standard size 1:1 (1080x1080px) that are ALL TEXT. We want the following quotes below on each graphic; one quote per graphic. AND, In very small letters at the bottom of each graphic, add @RKMarlowLive

The look and feel of these graphics should be complimentary to the color palette attached below; but keep them simple. But the design is up to you; at the end of this document, I provided various samples of all text graphics that I like as examples.

Target Market(s)

women looking to lose weight

Industry/Entity Type

health and wellness

Colors
E54698
E96AAD
F1A4CE
F9D9EA
FCEFF6

Requirements
Must have
• the quotes in the document
Should not have
• no stock photography

```html
<!DOCTYPE html>
<html lang="en">
<head>
<meta charset="utf-8">
<title>Natural Solution – Quote Graphic</title>
<link rel="stylesheet" href="https://fonts.googleapis.com/css2?family=Inter:wght@800&family=Italiana&display=swap">
<style>
  :root {
    --bg: #ffffff;
    --headline: #d4006f;
    --headline-glow: #34e3f0;
    --ink: #111111;
    --spark: #ff9fcf;
  }
  html, body {
    margin: 0;
    padding: 0;
    width: 1200px;
    height: 1200px;
    overflow: hidden;
    background: var(--bg);
  }
  .graphic {
    position: relative;
    width: 1200px;
    height: 1200px;
    background: var(--bg);
  }
  .headline-line {
    position: absolute;
    left: 92px;
    margin: 0;
    font-family: "Inter", "Helvetica Neue", Arial, sans-serif;
    font-weight: 800;
    font-size: 89px;
    line-height: 1;
    letter-spacing: -0.045em;
    color: var(--headline);
    text-shadow: -3px -1px 0 var(--headline-glow);
    white-space: nowrap;
  }
  .headline-line--first { top: 140px; }
  .headline-line--second { top: 262px; }

  .quote-line {
    position: absolute;
    left: 90px;
    margin: 0;
    font-family: "Italiana", "Didot", serif;
    font-weight: 400;
    font-size: 116px;
    line-height: 1;
    letter-spacing: 0.03em;
    color: var(--ink);
    white-space: nowrap;
  }
  .quote-line--1 { top: 418px; }
  .quote-line--2 { top: 541px; }
  .quote-line--3 { top: 664px; }
  .quote-line--4 { top: 786px; }

  .sparkle {
    position: absolute;
    left: 1066px;
    top: 683px;
    width: 112px;
    height: 112px;
  }
  .handle {
    position: absolute;
    left: 94px;
    top: 1088px;
    margin: 0;
    font-family: "Inter", "Helvetica Neue", Arial, sans-serif;
    font-weight: 800;
    font-size: 28px;
    line-height: 1;
    letter-spacing: -0.01em;
    color: var(--ink);
  }
</style>
</head>
<body>
  <main class="graphic">
    <h1 class="headline">
      <span class="headline-line headline-line--first">Finally,</span>
      <span class="headline-line headline-line--second">A natural solution</span>
    </h1>
    <p class="quote">
      <span class="quote-line quote-line--1">THAT FLATTENS</span>
      <span class="quote-line quote-line--2">YOUR BELLY</span>
      <span class="quote-line quote-line--3">AND EASES</span>
      <span class="quote-line quote-line--4">STOMACH BLOAT</span>
    </p>
    <svg class="sparkle" viewBox="-50 -50 100 100" aria-hidden="true">
      <polygon fill="var(--spark)" points="0,-50 5,-18 22,-43 13,-13 43,-25 17,-4 50,0 17,4 43,25 13,13 22,43 5,18 0,50 -5,18 -22,43 -13,13 -43,25 -17,4 -50,0 -17,-4 -43,-25 -13,-13 -22,-43 -5,-18"/>
    </svg>
    <p class="handle">@RKMARLOWLIVE</p>
  </main>
</body>
</html>
```